Varolink Signal Systems Website Design

We are an Australian based telecommunications company who specialise in the design, build and implementation of mission critical communications infrastructure. We have offices throughout Australia, New Zealand and Europe. Our Customers are operators in multiple markets from Oil & Gas, Mining, Government, Utilities, Carrier & Transportation.

We also work with large multi-national companies, that provide telecommunication and services such as; Threnvo, Maldquist, Pelva, Bramwick and many more. We want to be able to achieve the same level of impressions and professionalism as what these companies present on their websites.

To reflect our recent move into the European market, we need our new site to reflect who we are as a company, and exhibit the fact we are not just based in Australia, but we are a global organisation. We want to have a fresh clean look, thats modern, dynamic and simple. Flat textures and colours are perfect for us to adapt to. A site that is based around content management, with a responsive design that can be used on all devices.

We have started to develop a basic design language that we would like to incorporate in our overall website design. We have attached some documents that highlight our design language and we can provide colour codes and fonts to ensure consistency.

Our existing site is: www.varolinkss-example.com. Please feel free to view and pick apart items. From this example, we would massive improvement in how the site looks, feels and functions. We also want social media to form a big part of our site, with the likes of posts from twitter and blogs posting capabilities.

If you require anymore information about Varolink or our requirements, please do not hesitate to contact.

Thanks and good luck!

Target Market(s)

Potential & Existing Customers, New international customers & markets, New Market Sectors, Partners, Service Providers

Industry/Entity Type

Telecommunications

Coding

Coded - Design and coding required

Number of Pages Required

5+ page

Font styles to use
Sans Serif

Requirements
Must have
• Content Management, Responsive Design for multiple device compatibility, Social media integration, use of lots of imagery, drop down menus, search capabilities
Should not have
• No flash.

```html
<!DOCTYPE html>
<html lang="en">
<head>
<meta charset="utf-8">
<title>Varolink Signal Systems</title>
<link href="https://fonts.googleapis.com/css2?family=Raleway:wght@600;700&family=Roboto:wght@300;400;500&display=swap" rel="stylesheet">
<style>
:root{
  --purple:#6a65a9;
  --purple-dark:#5f5a9d;
  --navy:#2b2a7c;
  --ink:#222;
  --text:#666;
  --muted:#888;
  --light:#f1f1f2;
  --footer-dark:#1d1d1d;
  --white:#fff;
}
*{margin:0;padding:0;box-sizing:border-box}
html,body{width:1200px;height:2356px;overflow:hidden}
body{font-family:"Roboto",Arial,sans-serif;color:var(--ink);background:var(--white);position:relative}
ul{list-style:none}
a{color:inherit;text-decoration:none}

.top-bar{height:11px;background:var(--purple)}
.site-header{position:relative;height:117px;background:var(--white);border-bottom:1px solid #e2e2e2}
.brand{position:absolute;left:88px;top:42px;display:flex;align-items:center;gap:10px;font-family:"Roboto",sans-serif;font-weight:500;font-size:30px;color:var(--ink)}
.brand-dot{width:14px;height:14px;border-radius:50%;background:var(--purple)}
.main-nav{position:absolute;right:149px;top:54px;display:flex;gap:34px;font-size:14.5px;color:#222}
.main-nav .active{color:var(--purple)}
.search-btn{position:absolute;left:1073px;top:44px;width:38px;height:39px;border:1px solid #555;display:flex;align-items:center;justify-content:center}

.hero{position:relative;height:568px;background:linear-gradient(160deg,#c8c9c6 0%,#9c9e9a 35%,#8d8a6a 55%,#5d5f60 75%,#a9aaa8 100%)}
.hero-copy{position:absolute;left:0;right:0;top:385px;text-align:center;color:var(--white);text-shadow:0 2px 6px rgba(0,0,0,.45)}
.hero-title{font-family:"Raleway",sans-serif;font-weight:700;font-size:47px;letter-spacing:.5px}
.hero-sub{font-family:"Raleway",sans-serif;font-weight:600;font-size:29px;margin-top:2px}
.hero-dots{position:absolute;top:668px;left:0;right:0;display:flex;justify-content:center;gap:7px}
.hero-dots span{width:12px;height:12px;border-radius:50%;background:var(--white)}
.hero-dots .on{background:var(--purple)}

.welcome{position:absolute;top:740px;left:96px;width:1008px;text-align:center}
.welcome h1{font-weight:400;font-size:26px;color:var(--ink)}
.welcome h1 span,.section-title span{color:var(--purple)}
.welcome p{margin-top:16px;font-size:13.6px;line-height:23px;color:var(--text);text-align:justify;text-align-last:center}

.pillar{position:absolute;top:922px;display:flex}
.pillar-icon{width:94px;height:94px;border:1.5px solid #444;border-radius:50%;display:flex;align-items:center;justify-content:center;flex:none}
.pillar-body{margin-left:16px;margin-top:7px;width:196px}
.pillar-body h3{font-weight:400;font-size:16.5px;color:var(--ink)}
.pillar-body p{margin-top:9px;font-size:11.5px;line-height:19px;color:var(--muted)}

.operations{position:absolute;top:1079px;left:0;width:1200px;height:393px;background:linear-gradient(120deg,#f6f6f7,#ececee 50%,#f5f5f6)}
.section-title{font-weight:400;font-size:21px;color:var(--ink)}
.operations .section-title{position:absolute;left:90px;top:54px}
.slider-arrows{position:absolute;display:flex;gap:4px}
.op-card{position:absolute;top:102px;width:246px}
.op-photo{height:157px;border:4px solid var(--white);box-shadow:0 1px 3px rgba(0,0,0,.25)}
.op-card h3{margin-top:19px;font-weight:400;font-size:14.5px;letter-spacing:.3px;color:#333}
.op-card p{margin-top:9px;font-size:11.5px;line-height:19px;color:var(--muted)}

.support{position:absolute;top:1472px;left:0;width:1200px;height:283px;background:linear-gradient(180deg,#2f3a4e 0%,#3b3f48 50%,#5a3b2a 100%);text-align:center;color:var(--white)}
.support h2{margin-top:48px;font-weight:500;font-size:37px;letter-spacing:.5px}
.support p{margin:12px auto 0;width:660px;font-size:16.5px;line-height:28px}
.support-btn{display:inline-block;margin-top:27px;width:137px;height:44px;line-height:42px;border:1.5px solid var(--white);border-radius:6px;font-size:16.5px}

.blog{position:absolute;top:1755px;left:0;width:1200px;height:295px}
.blog .section-title{position:absolute;left:96px;top:54px;font-size:22px}
.blog .section-title span{color:var(--navy)}
.post{position:absolute;top:108px;display:flex}
.post-photo{position:relative;width:212px;height:141px;border:4px solid var(--white);box-shadow:0 1px 4px rgba(0,0,0,.3);flex:none}
.post-tag{position:absolute;left:8px;bottom:8px;display:flex;align-items:center;gap:5px;font-size:11.5px;color:var(--white)}
.post-body{margin-left:16px;width:230px}
.post-body h3{margin-top:8px;font-weight:400;font-size:13px;color:var(--ink)}
.post-date{margin-top:8px;font-size:10.5px;color:var(--purple)}
.post-body p{margin-top:6px;font-size:10px;line-height:18px;color:var(--muted)}
.read-more{display:block;margin-top:8px;font-size:11px;color:var(--navy)}

.site-footer{position:absolute;top:2050px;left:0;width:1200px;height:220px;background:var(--purple-dark);color:var(--white)}
.foot-col{position:absolute;top:44px}
.foot-col h4{font-weight:500;font-size:14.5px;letter-spacing:.3px}
.foot-links{margin-top:19px}
.foot-links li{font-size:12px;line-height:24px;display:flex;align-items:center;gap:7px}
.foot-links li::before{content:"";border-left:4px solid var(--white);border-top:3px solid transparent;border-bottom:3px solid transparent}
.tweet{margin-top:19px;display:flex;gap:14px}
.tweet-mark{width:18px;height:18px;background:var(--white);border-radius:3px;flex:none}
.tweet p{font-size:11.5px;line-height:21px;width:208px}
.contact-list{margin-top:19px;font-size:12px;line-height:21px}
.contact-list li{margin-bottom:9px}
.newsletter p{margin-top:18px;font-size:12px;line-height:17px;width:210px}
.news-form{margin-top:13px;display:flex}
.news-form span{width:145px;height:30px;background:#ececec;color:#777;font-size:11.5px;line-height:30px;padding-left:13px}
.news-form b{width:58px;height:30px;background:#222;color:var(--white);font-weight:400;font-size:11.5px;line-height:30px;text-align:center}

.bottom-bar{position:absolute;top:2270px;left:0;width:1200px;height:86px;background:var(--footer-dark);color:var(--white)}
.copyright{position:absolute;left:86px;top:34px;font-size:12.5px}
.social{position:absolute;left:977px;top:26px;display:flex;gap:9px}
.social span{width:26px;height:26px;background:#8a86bd;border-radius:2px}
</style>
</head>
<body>
<div class="top-bar"></div>
<header class="site-header">
  <a class="brand" href="#"><span>Varolink</span><span class="brand-dot"></span></a>
  <nav>
    <ul class="main-nav">
      <li class="active">HOME</li>
      <li>PRODUCTS &amp; SERVICES</li>
      <li>SECTORS</li>
      <li>SUPPORT</li>
      <li>CORPORATE</li>
      <li>CONTACT</li>
    </ul>
  </nav>
  <div class="search-btn">
    <svg width="14" height="14" viewBox="0 0 14 14"><circle cx="6" cy="6" r="4.3" fill="none" stroke="#333" stroke-width="2"/><line x1="9.2" y1="9.2" x2="13" y2="13" stroke="#333" stroke-width="2.2"/></svg>
  </div>
</header>

<section class="hero" role="img" aria-label="Open-plan office with engineers working at computer desks">
  <div class="hero-copy">
    <div class="hero-title">VAROLINK SIGNAL SYSTEMS</div>
    <div class="hero-sub">Neque porro quisquam est qui dolorem ipsum quia</div>
  </div>
</section>
<div class="hero-dots"><span></span><span></span><span class="on"></span><span></span><span></span></div>

<section class="welcome">
  <h1>WELCOME TO <span>VAROLINK SIGNAL SYSTEMS</span></h1>
  <p>We are an Australian based telecommunications company who specialise in the design, build and implementation of mission critical communications infrastructure. We have offices throughout Australia, New Zealand and Europe. Our Customers are operators in multiple markets from Oil &amp; Gas, Mining, Government, Utilities, Carrier &amp; Transportation. We also work with large multinational companies, that provide telecommunication and services such as;</p>
</section>

<div class="pillar" style="left:91px">
  <div class="pillar-icon">
    <svg width="30" height="30" viewBox="0 0 30 30"><circle cx="15" cy="9" r="6.5" fill="var(--purple)"/><path d="M3 29c0-8 5-12 12-12s12 4 12 12z" fill="var(--purple)"/></svg>
  </div>
  <div class="pillar-body"><h3>OUR VISION</h3><p>To be a leading international provider of advanced and engineered solutions for mission and business</p></div>
</div>
<div class="pillar" style="left:449px">
  <div class="pillar-icon">
    <svg width="28" height="36" viewBox="0 0 28 36"><path d="M14 2a11 11 0 0 0-6 20v5h12v-5a11 11 0 0 0-6-20z" fill="none" stroke="var(--purple)" stroke-width="2.5"/><rect x="9" y="29" width="10" height="3" fill="var(--purple)"/><path d="M14 22v-9l-3-3m3 3 3-3" fill="none" stroke="var(--purple)" stroke-width="2"/></svg>
  </div>
  <div class="pillar-body"><h3>OUR MARKETS</h3><p>Varolink specialises in design and development of systems and networks that meet the stringent requirements</p></div>
</div>
<div class="pillar" style="left:801px">
  <div class="pillar-icon">
    <svg width="34" height="34" viewBox="0 0 34 34"><path d="M32 2 2 15l11 4 4 12z" fill="var(--purple)"/><path d="M32 2 13 19" stroke="#fff" stroke-width="1.5"/></svg>
  </div>
  <div class="pillar-body"><h3>OUR BUSINESSES</h3><p>Varolink's core businesses are structured into functional teams, each offering a varied</p></div>
</div>

<section class="operations">
  <h2 class="section-title">OPERATIONS <span>MANAGEMENT</span></h2>
  <div class="slider-arrows" style="left:1083px;top:60px">
    <svg width="30" height="16" viewBox="0 0 30 16"><path d="M9 2 3 8l6 6M21 2l6 6-6 6" fill="none" stroke="#111" stroke-width="2"/></svg>
  </div>
  <article class="op-card" style="left:93px">
    <div class="op-photo" role="img" aria-label="Businessman reviewing documents in an archive" style="background:linear-gradient(135deg,#8a6a55,#c9b8a8 55%,#5b4a40)"></div>
    <h3>QUALITY ASSURANCE</h3>
    <p>Varolink strives for excellence in health and safety management.</p>
  </article>
  <article class="op-card" style="left:350px">
    <div class="op-photo" role="img" aria-label="Site workers in hard hats and safety vests" style="background:linear-gradient(135deg,#c9c9c4,#d98a3a 50%,#e3c43a)"></div>
    <h3>HEALTH &amp; SAFETY</h3>
    <p>Varolink is committed to conducting business in an environmentally aware and</p>
  </article>
  <article class="op-card" style="left:608px">
    <div class="op-photo" role="img" aria-label="Rocky coastline with orange lichen" style="background:linear-gradient(180deg,#9fb6c8,#6d8a9b 35%,#a96238 65%,#5a4a3e)"></div>
    <h3>ENVIRONMENT</h3>
    <p>Varolink is committed to conducting business in an environmentally aware and</p>
  </article>
  <article class="op-card" style="left:865px">
    <div class="op-photo" role="img" aria-label="Technician working at a server rack" style="background:linear-gradient(135deg,#2c3432,#4a6a60 50%,#7a7f8a)"></div>
    <h3>INFORMATION SECURITY</h3>
    <p>Varolink is well aware of the importance of Network and Information security and has</p>
  </article>
</section>

<section class="support" role="img" aria-label="Solar-powered communications site in outback terrain">
  <h2>TECHNICAL SUPPORT</h2>
  <p>Varolink offers flexible multi-technology and multi-vendor support services. We take an end-to-end view of networks, helping you to resolve issues quickly and completely.</p>
  <a class="support-btn" href="#">Click Here</a>
</section>

<section class="blog">
  <h2 class="section-title">LATEST <span>BLOG</span></h2>
  <div class="slider-arrows" style="left:1084px;top:51px">
    <svg width="22" height="14" viewBox="0 0 22 14"><path d="M7 2 2 7l5 5M15 2l5 5-5 5" fill="none" stroke="#111" stroke-width="1.8"/></svg>
  </div>
  <article class="post" style="left:94px">
    <div class="post-photo" role="img" aria-label="Red locomotive beside a harbour pipeline" style="background:linear-gradient(180deg,#8fb3d3 0%,#7d8ea0 40%,#a8463a 55%,#5b5b5b 100%)">
      <span class="post-tag"><svg width="14" height="16" viewBox="0 0 14 16"><path d="M7 1C4 6 2 8 2 11a5 5 0 0 0 10 0c0-3-2-5-5-10z" fill="none" stroke="#fff" stroke-width="1.5"/></svg>Oil &amp; Gas</span>
    </div>
    <div class="post-body">
      <h3>SIMPLY DUMMY TEXT</h3>
      <div class="post-date">20/08/2016</div>
      <p>Lorem Ipsum has been the industry's standard dummy text ever since the 1500s, when an unknown printer took a galley of type and scrambled it to make a type specimen book.</p>
      <a class="read-more" href="#">Read More &gt;&gt;</a>
    </div>
  </article>
  <article class="post" style="left:617px">
    <div class="post-photo" role="img" aria-label="Arched bridge over a river with city buildings" style="background:linear-gradient(180deg,#9cc0e0 0%,#c4d6e6 45%,#6f7c86 75%,#3f4a52 100%)">
      <span class="post-tag"><svg width="16" height="14" viewBox="0 0 16 14"><path d="M1 13h14M3 13V6h3v7M7 13V2h3v11M11 13V8h3v5" fill="none" stroke="#fff" stroke-width="1.3"/></svg>Utilities</span>
    </div>
    <div class="post-body">
      <h3>SIMPLY DUMMY TEXT</h3>
      <div class="post-date">20/08/2016</div>
      <p>Lorem Ipsum has been the industry's standard dummy text ever since the 1500s, when an unknown printer took a galley of type and scrambled it to make a type specimen book.</p>
      <a class="read-more" href="#">Read More &gt;&gt;</a>
    </div>
  </article>
</section>

<footer class="site-footer">
  <div class="foot-col" style="left:96px">
    <h4>LINKS</h4>
    <ul class="foot-links">
      <li>Customer Support</li>
      <li>Documentation</li>
      <li>Resources</li>
      <li>General FAQs</li>
      <li>Shortcodes</li>
    </ul>
  </div>
  <div class="foot-col" style="left:309px">
    <h4>LATEST TWEET`S</h4>
    <div class="tweet">
      <span class="tweet-mark"></span>
      <p>Phasellus porta. Fusce susct varius mi. Cum sociis natoque penabus et magnis dis parturient montes, nascetur ridiculus mus. See more here http://lnk.example/Vr4kq2</p>
    </div>
  </div>
  <div class="foot-col" style="left:647px">
    <h4>GET IN TOUCH</h4>
    <ul class="contact-list">
      <li>Address : 27 Larkfield Row, Brenmoor,<br>Ontario K9X4T2</li>
      <li>Phone : 1 800 555-0147</li>
      <li>Email : info@varolink-example.com</li>
    </ul>
  </div>
  <div class="foot-col newsletter" style="left:905px">
    <h4>NEWSLETTER</h4>
    <p>Your about us information would fit here nicely.</p>
    <div class="news-form"><span>Email address</span><b>Submit</b></div>
  </div>
</footer>

<div class="bottom-bar">
  <div class="copyright">© 2016 All Rights Reserved</div>
  <div class="social"><span></span><span></span><span></span><span></span></div>
</div>
</body>
</html>
```